Business card design needed

I need a business card design for a dog walking, dog minding and dog training business. Please refer to my website for the basic company colours and fonts I'm after. Planning on a double sided card, so all information doesn't need to be on the 'front' side.
Cheers

Industry/Entity Type

Dog Training

Contact Information for Business Card

Meadow Paws - happy hounds
Rua 0498307164
meadowpawsdemo.com.au
-walking
-holiday stays
-onsite care
-training and behavioural consultations

```html
<!DOCTYPE html>
<html lang="en">
<head>
<meta charset="utf-8">
<title>Meadow Paws – happy hounds</title>
<link rel="stylesheet" href="https://fonts.googleapis.com/css2?family=Exo+2:ital,wght@0,300;1,300;1,700&display=swap">
<style>
  :root {
    --brand-orange: #e55a25;
    --orange-light: #ec6a36;
    --orange-deep: #d9511f;
    --ink-white: #ffffff;
    --slate: #5e5e60;
  }
  html, body {
    margin: 0;
    padding: 0;
    width: 1200px;
    height: 692px;
    overflow: hidden;
    background: var(--brand-orange);
  }
  .card {
    position: relative;
    width: 1200px;
    height: 692px;
    background: var(--brand-orange);
    overflow: hidden;
    font-family: "Exo 2", sans-serif;
    color: var(--ink-white);
  }
  .dog-artwork {
    position: absolute;
    left: 0;
    top: 30px;
    width: 430px;
    height: 662px;
    background: linear-gradient(160deg, var(--orange-light) 0%, var(--brand-orange) 55%, var(--orange-deep) 100%);
    border-top-right-radius: 140px;
  }
  .values {
    position: absolute;
    top: 32px;
    right: 45px;
    margin: 0;
    width: 680px;
    text-align: right;
    font-size: 40px;
    line-height: 58px;
    font-style: italic;
    font-weight: 300;
    letter-spacing: 0.2px;
  }
  .values strong {
    font-weight: 700;
  }
  .brand {
    position: absolute;
    left: 322px;
    top: 458px;
    margin: 0;
  }
  .brand-name {
    display: block;
    font-size: 114px;
    line-height: 1;
    font-weight: 300;
    font-style: normal;
    letter-spacing: 1px;
    text-transform: uppercase;
    white-space: nowrap;
    color: var(--ink-white);
  }
  .brand-tagline {
    display: block;
    margin-top: 8px;
    padding-left: 6px;
    font-size: 46px;
    line-height: 1;
    font-weight: 300;
    color: var(--ink-white);
  }
</style>
</head>
<body>
  <main class="card">
    <div class="dog-artwork" role="img" aria-label="Line illustration of a standing dog in profile wearing a collar and lead"></div>

    <p class="values">We’re about a <strong>good balance</strong> of <strong>fun,<br>exercise, proper stimulation</strong> and<br><strong>reinforcing good habits</strong> and<br><strong>canine manners</strong></p>

    <h1 class="brand">
      <span class="brand-name">Meadow Paws</span>
      <span class="brand-tagline">happy hounds</span>
    </h1>
  </main>
</body>
</html>
```